KV HOLDING Business Cards

I need business cards for "KV Holding group LLC" doublesided... logo on the back (also include logo on front)
logo attached to project... i have jpg up..
Company Info:
418 East Marlow Avenue, Suite 7B
Chicago, Illinois 60617
facsimile 312-555-0188 (list fax, address, website on all cards.)
www.kvholdinggroup.example
Three different people on cards:
Dorian P. Kell, CPA MST
Principal
ofc 312-555-0142
mobile 312-555-0167
dorianpkell@kvholdinggroup.example
Marcus T. Brenholt, CPA MST
Principal
marcustbrenholt@kvholdinggroup.example
mobile 708-555-0119
ofc 312-555-0142
Nigel F Carrow
Principal
ofc 312-555-0142
no mobile
nigelfcarrow@kvholdinggroup.example
I have multiple projects listed.. see below:
Business cards for amber gate equity llc
letterhead
envelopes
Business cards for KV Holding LLC
letterhead
envelopes
Target Market(s)
rich people
Industry/Entity Type
Business
Look and feel

```html
<!DOCTYPE html>
<html lang="en">
<head>
<meta charset="utf-8">
<title>KV Holding Group LLC – Business Cards</title>
<link rel="stylesheet" href="https://fonts.googleapis.com/css2?family=Arimo:wght@400&family=Marcellus&display=swap">
<style>
  :root {
    --stage: #3b3b3b;
    --navy: #163f72;
    --card-grey: #c6c6c6;
    --white: #ffffff;
    --brand-font: "Marcellus", serif;
    --text-font: "Arimo", sans-serif;
  }
  * { margin: 0; padding: 0; box-sizing: border-box; }
  html, body { width: 1200px; height: 1000px; overflow: hidden; }
  body { background: var(--stage); position: relative; }

  .card { position: absolute; height: 292px; overflow: hidden; }
  .card-back { left: 77px; width: 499px; background: var(--card-grey); }
  .card-front { left: 631px; width: 500px; background: var(--navy); }
  .row-1 { top: 31px; }
  .row-2 { top: 348px; }
  .row-3 { top: 667px; }

  .brand-mark { position: absolute; border-radius: 50%; background: var(--navy); }
  .card-back .brand-mark { width: 120px; height: 120px; left: 190px; top: 40px; }
  .card-back .brand-name {
    position: absolute; left: 0; right: 0; top: 184px; text-align: center;
    font-family: var(--brand-font); font-size: 32px; color: var(--navy); letter-spacing: 1px;
  }
  .card-back .brand-web {
    position: absolute; left: 0; right: 0; top: 224px; text-align: center;
    font-family: var(--brand-font); font-size: 21px; color: var(--navy); letter-spacing: 3px;
  }

  .front-head { position: absolute; left: 0; top: 0; width: 100%; height: 127px; background: var(--white); }
  .card-front .brand-mark { width: 62px; height: 62px; left: 219px; top: 28px; }
  .card-front .brand-name {
    position: absolute; left: 0; right: 0; top: 97px; text-align: center;
    font-family: var(--brand-font); font-size: 17px; color: var(--navy);
  }

  .person {
    position: absolute; left: 0; right: 0; top: 139px; text-align: center;
    font-family: var(--text-font); color: var(--white);
  }
  .person-name { font-size: 20px; line-height: 24px; }
  .person-role { font-size: 12px; line-height: 14px; margin-bottom: 8px; }
  .contact-list { list-style: none; font-size: 11px; line-height: 14px; }
  .company-address {
    position: absolute; left: 0; right: 0; bottom: 16px; text-align: center;
    font-family: var(--text-font); font-size: 10.5px; color: var(--white);
  }
</style>
</head>
<body>

  <section class="card card-back row-1">
    <div class="brand-mark"></div>
    <div class="brand-name">KV HOLDING GROUP LLC</div>
    <div class="brand-web">www.kvholdinggroup.example</div>
  </section>
  <section class="card card-front row-1">
    <div class="front-head">
      <div class="brand-mark"></div>
      <div class="brand-name">KV HOLDING GROUP LLC</div>
    </div>
    <div class="person">
      <div class="person-name">Dorian P. Kell, CPA MST</div>
      <div class="person-role">Principal</div>
      <ul class="contact-list">
        <li>Office : 312-555-0142</li>
        <li>Direct : 312-555-0173</li>
        <li>Mobile : 312-555-0167</li>
        <li>Facsimile : 312-555-0188</li>
        <li>Email : dorianpkell@kvholdinggroup.example</li>
      </ul>
    </div>
    <div class="company-address">418 East Marlow Avenue, Suite 7B Chicago, Illinois 60617 | www.kvholdinggroup.example</div>
  </section>

  <section class="card card-back row-2">
    <div class="brand-mark"></div>
    <div class="brand-name">KV HOLDING GROUP LLC</div>
    <div class="brand-web">www.kvholdinggroup.example</div>
  </section>
  <section class="card card-front row-2">
    <div class="front-head">
      <div class="brand-mark"></div>
      <div class="brand-name">KV HOLDING GROUP LLC</div>
    </div>
    <div class="person">
      <div class="person-name">Marcus T. Brenholt, CPA MST</div>
      <div class="person-role">Principal</div>
      <ul class="contact-list">
        <li>Office : 312-555-0142</li>
        <li>Mobile : 708-555-0119</li>
        <li>Facsimile : 312-555-0188</li>
        <li>Email : marcustbrenholt@kvholdinggroup.example</li>
      </ul>
    </div>
    <div class="company-address">418 East Marlow Avenue, Suite 7B Chicago, Illinois 60617 | www.kvholdinggroup.example</div>
  </section>

  <section class="card card-back row-3">
    <div class="brand-mark"></div>
    <div class="brand-name">KV HOLDING GROUP LLC</div>
    <div class="brand-web">www.kvholdinggroup.example</div>
  </section>
  <section class="card card-front row-3">
    <div class="front-head">
      <div class="brand-mark"></div>
      <div class="brand-name">KV HOLDING GROUP LLC</div>
    </div>
    <div class="person">
      <div class="person-name">Nigel F Carrow</div>
      <div class="person-role">Principal</div>
      <ul class="contact-list">
        <li>Office : 312-555-0142</li>
        <li>Facsimile : 312-555-0188</li>
        <li>Email : nigelfcarrow@kvholdinggroup.example</li>
      </ul>
    </div>
    <div class="company-address">418 East Marlow Avenue, Suite 7B Chicago, Illinois 60617 | www.kvholdinggroup.example</div>
  </section>

</body>
</html>
```